Morning Harbor Community Chapel needs a new Business Card/Letterhead Suite

***** IT DOES NOT HAVE TO FEATURE GREEN AND BROWN in order to be a successful design*****

****FONTS: SF New Republic, 'Morning Harbor'; Nexa Light, 'Community Chapel'****

***We have two locations, with two addresses. So the business card AND letterhead need to include two sets of address information***

We are a growing church in New York in need of a new stationary suite. We have recently adopted a new logo (via a successful PixelGuild project) and need new business cards, letterhead, envelopes, and folders.

We would like to see creative, original designs that are modern and clean/elegant (NOT dated "churchy" graphics that are cheesy).

We need this project worked on immediately, as we need to print new business cards for upcoming programs we have on our schedule. So, the designs need to be solid so that we can move quickly throughout the revision process toward print.

We'd also need editables files, so that we can drop in other staff members names/phone numbers, to be able to print cards for those staff needing them.

Requirements
Must have
• Our logo
• Must be given to us in an editable format (to change names)
Nice to have
• Some examples on grey, or recycled, card stock
• card stock (background) does not have to be white
Should not have
• Any extraneous logo's or symbols

```html
<!DOCTYPE html>
<html lang="en">
<head>
<meta charset="utf-8">
<title>Morning Harbor Community Chapel – Presentation Folder</title>
<link href="https://fonts.googleapis.com/css2?family=Questrial&family=Open+Sans:wght@400&display=swap" rel="stylesheet">
<style>
  :root {
    --backdrop: #bdbcbd;
    --green-deep: #2d5f2b;
    --green-mid: #3f7b3b;
    --green-brand: #3c7a36;
    --brown: #5e5a3a;
    --paper: #ffffff;
    --paper-shade: #ededed;
    --ink-light: #e9f0e6;
  }
  * { box-sizing: border-box; margin: 0; padding: 0; }
  html, body { width: 1200px; height: 1090px; overflow: hidden; }
  body {
    background: var(--backdrop);
    font-family: 'Open Sans', sans-serif;
    position: relative;
  }
  .folder-spread {
    position: absolute;
    left: 120px;
    top: 205px;
    width: 960px;
    height: 680px;
    display: flex;
    box-shadow: 0 18px 40px rgba(0,0,0,0.25);
  }
  .panel { position: relative; width: 480px; height: 680px; overflow: hidden; }

  /* Back cover */
  .back-cover {
    background: linear-gradient(115deg, var(--green-deep) 0%, var(--green-mid) 45%, var(--green-deep) 100%);
  }
  .back-cover__watermark {
    position: absolute;
    left: 0; right: 0;
    top: 250px;
    text-align: center;
    font-family: 'Questrial', sans-serif;
    font-size: 30px;
    line-height: 1.3;
    color: rgba(255,255,255,0.08);
  }
  .contact {
    position: absolute;
    right: 40px;
    bottom: 48px;
    color: var(--ink-light);
    font-size: 9.5px;
    line-height: 1.6;
    text-align: left;
  }
  .contact__row { display: flex; align-items: center; gap: 12px; }
  .contact__item { display: inline-flex; align-items: center; gap: 4px; }
  .contact__item svg { width: 9px; height: 9px; fill: var(--ink-light); }
  .contact__address { padding-left: 72px; }

  /* Front cover */
  .front-cover {
    background: linear-gradient(160deg, var(--paper) 55%, var(--paper-shade) 100%);
  }
  .wordmark {
    position: absolute;
    left: 0; right: 0;
    top: 245px;
    text-align: center;
    font-family: 'Questrial', sans-serif;
    font-weight: 400;
    color: var(--green-brand);
  }
  .wordmark__name { display: block; font-size: 44px; line-height: 1; letter-spacing: -0.5px; }
  .wordmark__sub { display: block; margin-top: 10px; font-size: 14px; letter-spacing: 6px; }
  .front-band {
    position: absolute;
    left: 0; right: 0; bottom: 0;
    height: 16px;
    background: var(--green-brand);
  }
  .front-band__tab {
    position: absolute;
    right: 0; bottom: 0;
    height: 16px;
    width: 170px;
    background: var(--brown);
    clip-path: polygon(8px 0, 100% 0, 100% 100%, 0 100%);
    color: var(--ink-light);
    font-size: 8.5px;
    line-height: 16px;
    text-align: center;
  }
</style>
</head>
<body>
  <main class="folder-spread">
    <section class="panel back-cover">
      <div class="back-cover__watermark" aria-hidden="true">Morning Harbor<br>Community Chapel</div>
      <div class="contact">
        <div class="contact__address">214 Harbor Lane, Suite 2 Port Jefferson, NY 11777</div>
        <div class="contact__row">
          <span class="contact__item">
            <svg viewBox="0 0 10 10"><path d="M2 0.5 L3.6 0.5 L4.2 2.8 L3 3.6 Q4 5.8 6.4 7 L7.2 5.8 L9.5 6.4 L9.5 8 Q9.5 9.5 8 9.5 Q0.5 8.8 0.5 2 Q0.5 0.5 2 0.5Z"/></svg>
            631-555-0148
          </span>
          <span class="contact__item">
            <svg viewBox="0 0 10 10"><path d="M0.5 2 H9.5 V8 H0.5Z M0.5 2 L5 5.5 L9.5 2" fill="none" stroke="#e9f0e6" stroke-width="1"/></svg>
            hello@morningharbor.org
          </span>
          <span class="contact__item">
            <svg viewBox="0 0 10 10"><circle cx="5" cy="5" r="4.3" fill="none" stroke="#e9f0e6" stroke-width="1"/><path d="M0.7 5 H9.3 M5 0.7 Q2.5 5 5 9.3 M5 0.7 Q7.5 5 5 9.3" fill="none" stroke="#e9f0e6" stroke-width="0.8"/></svg>
            www.morningharborchapel.org
          </span>
        </div>
      </div>
    </section>

    <section class="panel front-cover">
      <h1 class="wordmark">
        <span class="wordmark__name">Morning Harbor</span>
        <span class="wordmark__sub">COMMUNITY CHAPEL</span>
      </h1>
      <div class="front-band">
        <div class="front-band__tab">www.websitename.com</div>
      </div>
    </section>
  </main>
</body>
</html>
```